Quimby's Yard & Garden Center Business Card Update

I need an updated Business card design for my Lawn and Garden Center. We do Landscaping installs, Lawn Mowing, Snow Removal and also have a Garden Center Retail Division. I uploaded a few of our previous business cards to give an idea of what we are starting with. The main goal of this update is to simplify and modernize the business card, not all of the services that are on the previous cards has to be on the new one but I would still like to highlight our main services. There is also a sample of our logo that Can be used in the design.

Industry/Entity Type

Landscaping

Contact Information for Business Card

Morris Quimby
Morris@Quimbysyardandgarden.example
Business (555) 201-7784
Cell (555) 318-6092

Colors

Designer to choose colors to be used in the design.

Requirements
Must have
• Services Provided :
• Landscaping
• Lawn Maintenance
• Snow Removal
• Garden Center

```html
<!DOCTYPE html>
<html lang="en">
<head>
<meta charset="utf-8">
<title>Quimby's Yard &amp; Garden Center – Business Card</title>
<link href="https://fonts.googleapis.com/css2?family=Lato:wght@400;700&display=swap" rel="stylesheet">
<style>
  :root {
    --backdrop: #dcdde1;
    --green-dark: #1f3b1d;
    --green-light: #3a6536;
    --green-brand: #2d5a27;
    --card-white: #f7f7f6;
    --ink: #2b2b2b;
    --on-green: #f2f2ee;
  }
  * { box-sizing: border-box; margin: 0; padding: 0; }
  html, body {
    width: 1200px; height: 800px; overflow: hidden;
    background: var(--backdrop);
    font-family: "Lato", sans-serif;
  }
  .canvas { position: relative; width: 1200px; height: 800px; }

  .card {
    position: absolute; left: 360px;
    width: 480px; height: 272px;
  }
  .card--front {
    top: 104px;
    background: linear-gradient(225deg, var(--green-light) 0%, #2b5026 50%, var(--green-dark) 100%);
    color: var(--on-green);
  }
  .card--back {
    top: 424px;
    background: var(--card-white);
    color: var(--ink);
  }

  /* front */
  .brand {
    display: flex; align-items: center; gap: 12px;
    font-weight: 700; white-space: nowrap;
  }
  .brand__dot { border-radius: 50%; flex: none; }
  .card--front .brand {
    position: absolute; left: 0; right: 0; top: 92px;
    justify-content: center;
    font-size: 54px; color: var(--on-green);
  }
  .card--front .brand__dot { width: 34px; height: 34px; background: var(--on-green); }

  .services {
    position: absolute; left: 0; right: 0; bottom: 14px;
    display: flex; justify-content: center; gap: 15px;
    list-style: none; font-size: 11.5px; color: var(--on-green);
  }
  .services li::before {
    content: ""; display: inline-block;
    width: 5px; height: 5px; border-radius: 50%;
    background: var(--on-green);
    margin-right: 5px; vertical-align: 2px;
  }

  /* back */
  .card--back .brand {
    position: absolute; left: 40px; top: 118px;
    font-size: 27px; color: var(--green-brand); gap: 8px;
  }
  .card--back .brand__dot { width: 18px; height: 18px; background: var(--green-brand); }

  .divider {
    position: absolute; left: 206px; top: 78px;
    width: 1.5px; height: 115px; background: var(--green-brand);
  }
  .contact { position: absolute; left: 218px; top: 74px; }
  .contact__name { font-size: 18px; font-weight: 700; color: var(--green-brand); line-height: 1.2; }
  .contact__title { font-size: 12px; line-height: 1.4; margin-bottom: 14px; }
  .contact__line { font-size: 12px; line-height: 16.5px; white-space: nowrap; }
  .contact__label { font-weight: 700; color: var(--green-brand); }
</style>
</head>
<body>
<main class="canvas">
  <section class="card card--front" aria-label="Business card front">
    <div class="brand"><span class="brand__dot"></span><span class="brand__name">Quimby's</span></div>
    <ul class="services">
      <li>Landscaping</li>
      <li>Lawn Maintenance</li>
      <li>Garden Center</li>
      <li>Snow Removal</li>
    </ul>
  </section>

  <section class="card card--back" aria-label="Business card back">
    <div class="brand"><span class="brand__dot"></span><span class="brand__name">Quimby's</span></div>
    <div class="divider"></div>
    <div class="contact">
      <p class="contact__name">Morris Quimby</p>
      <p class="contact__title">Director</p>
      <p class="contact__line">(555) 201-7784 <span class="contact__label">Business</span></p>
      <p class="contact__line">(555) 318-6092 <span class="contact__label">Cell</span></p>
      <p class="contact__line">Morris@Quimbysyardandgarden.example</p>
      <p class="contact__line">www.quimbysyardandgarden.example</p>
    </div>
  </section>
</main>
</body>
</html>
```